LLC needs a business card design that emphasizes consulting and expert witness in upstream oil and g

I need a business card design for my company called Velmo Consultative Service, LLC. My expertise is in oil and gas upstream operations management to optimize performance and also as an expert witness for law firms in oil and gas upstream operations litigation.
The final design should communicate knowledge and hands-on experience as well as trust. (Velmo means rope or lasso. Perhaps "Velmo" should be in the form of a rope.) I do not like the color green in any shade. My first preference would be some shade of blue.

```html
<!DOCTYPE html>
<html lang="en">
<head>
<meta charset="utf-8">
<title>Velmo – Business Card</title>
<link rel="stylesheet" href="https://fonts.googleapis.com/css2?family=Open+Sans:wght@400;600;700&display=swap">
<style>
  :root {
    --backdrop: #ececec;
    --ink: #1c1c1e;
    --black-deep: #0e0e10;
    --black-soft: #3a3a3e;
    --paper: #ffffff;
    --accent-blue: #1d74b5;
    --glow-blue: #4fb3ea;
  }
  * { box-sizing: border-box; margin: 0; padding: 0; }
  html, body {
    width: 1200px;
    height: 800px;
    overflow: hidden;
    background: var(--backdrop);
    font-family: "Open Sans", Arial, sans-serif;
    color: var(--ink);
  }
  .canvas {
    position: relative;
    width: 1200px;
    height: 800px;
  }
  .card {
    position: absolute;
    top: 257px;
    width: 500px;
    height: 286px;
    overflow: hidden;
    box-shadow: 0 4px 14px rgba(0,0,0,0.18);
  }
  .card--front { left: 75px; }
  .card--back  { left: 625px; background: var(--paper); }

  .front-artwork {
    position: absolute;
    inset: 0;
    background: radial-gradient(ellipse at 45% 40%, var(--black-soft) 0%, #1f1f22 45%, var(--black-deep) 100%);
  }
  .brand {
    position: absolute;
    left: 50%;
    top: 50%;
    transform: translate(-50%, -50%);
    display: flex;
    align-items: center;
    gap: 12px;
  }
  .brand__dot {
    width: 14px;
    height: 14px;
    border-radius: 50%;
    background: var(--accent-blue);
  }
  .brand__name {
    font-size: 30px;
    font-weight: 400;
    color: var(--paper);
    line-height: 1;
  }

  .back-band {
    position: absolute;
    inset: 0;
    width: 100%;
    height: 100%;
  }
  .contact {
    position: absolute;
    left: 42px;
    top: 170px;
  }
  .contact__name {
    font-size: 19px;
    font-weight: 400;
    color: var(--ink);
    line-height: 1.1;
  }
  .contact__role {
    margin-top: 2px;
    margin-left: 18px;
    font-size: 9px;
    font-weight: 700;
    letter-spacing: 2px;
    color: var(--accent-blue);
  }
  .contact__list {
    list-style: none;
    margin-top: 10px;
    font-size: 11.5px;
    line-height: 1.45;
  }
  .contact__list li { display: flex; }
  .contact__label {
    width: 18px;
    font-weight: 700;
    font-size: 10px;
    color: var(--accent-blue);
  }
</style>
</head>
<body>
  <main class="canvas">
    <section class="card card--front">
      <div class="front-artwork" role="img" aria-label="Dark black liquid splash photograph"></div>
      <div class="brand">
        <span class="brand__dot" aria-hidden="true"></span>
        <p class="brand__name">Velmo</p>
      </div>
    </section>

    <section class="card card--back">
      <svg class="back-band" viewBox="0 0 500 286" aria-hidden="true">
        <defs>
          <linearGradient id="bandFill" x1="0" y1="0" x2="1" y2="1">
            <stop offset="0" stop-color="#2a2a2d"/>
            <stop offset="0.6" stop-color="#0f0f11"/>
            <stop offset="1" stop-color="#1a1a1c"/>
          </linearGradient>
          <filter id="edgeGlow" x="-10%" y="-50%" width="120%" height="200%">
            <feGaussianBlur stdDeviation="3"/>
          </filter>
        </defs>
        <path d="M0 0 H500 V45 C390 60 250 80 140 115 C80 134 35 150 0 160 Z" fill="url(#bandFill)"/>
        <path d="M500 45 C390 60 250 80 140 115 C80 134 35 150 0 160" fill="none" stroke="var(--glow-blue)" stroke-width="6" opacity="0.55" filter="url(#edgeGlow)"/>
        <path d="M500 45 C390 60 250 80 140 115 C80 134 35 150 0 160" fill="none" stroke="var(--accent-blue)" stroke-width="2"/>
      </svg>
      <div class="contact">
        <h1 class="contact__name">Name Surname</h1>
        <p class="contact__role">POSITION</p>
        <ul class="contact__list">
          <li><span class="contact__label">M</span>+00 00 000 00 00</li>
          <li><span class="contact__label">E</span>name.surname@velmo.com</li>
          <li><span class="contact__label">W</span>www.velmo.com</li>
        </ul>
      </div>
    </section>
  </main>
</body>
</html>
```